Gather the Orchard Gala Graphic Design

I’m seeking a professional graphic designer experienced in event branding to create a cohesive suite of materials for our third annual fundraising gala, “Gather the Orchard.” This year's theme is " An Evening in Linen to Gather the Orchard" Need to design collateral for website, social media and email blasts.
Target Market(s)
Affluent gala attendees
Industry/Entity Type
Fundraising / Charity / Outdoors / Sports
Font styles to use
Decorative
Script
Colors
0054AA
0677BA
7BADD7
CADEEF
E8F1F8
0094D4
00A9DD
6FCCEA
C7EBF8
E9F6FB
00AB8E
00BBA5
67D7C9
C6EFE9
E9F9F6
6B429C
8869AF
B7A5CE
E3DAEB
F3F0F8

```html
<!DOCTYPE html>
<html lang="en">
<head>
<meta charset="utf-8">
<title>Gather the Orchard Gala – Collateral Suite</title>
<link href="https://fonts.googleapis.com/css2?family=Cinzel+Decorative:wght@400;700&family=Great+Vibes&family=Montserrat:wght@400;500;600;700&display=swap" rel="stylesheet">
<style>
:root{
  --stage:#0d1b27;
  --navy:#0b2236;
  --deep:#123a5a;
  --mid:#3f7aa3;
  --sky:#9cc6e2;
  --pale:#cadeef;
  --mist:#e8f1f8;
  --white:#ffffff;
  --gold:#f2c94c;
  --gold-deep:#c9962a;
  --band:#08192a;
}
*{margin:0;padding:0;box-sizing:border-box}
html,body{width:748px;height:1200px;overflow:hidden;background:var(--stage)}
.canvas{position:relative;width:748px;height:1200px;background:var(--stage);font-family:"Montserrat",sans-serif;color:var(--white)}
.poster{position:absolute;overflow:hidden;text-align:center;
  background:linear-gradient(180deg,var(--navy) 0%,var(--deep) 30%,var(--mid) 58%,var(--sky) 72%,var(--deep) 86%,var(--band) 100%)}
.poster--hero{left:152px;top:45px;width:443px;height:572px;
  background:linear-gradient(180deg,var(--navy) 0%,var(--deep) 30%,var(--mid) 56%,var(--sky) 74%,var(--pale) 88%,var(--band) 89%)}
.poster--invite{left:50px;top:643px;width:304px;height:524px}
.poster--vip{left:394px;top:643px;width:304px;height:524px}
.poster__frame{position:absolute;inset:10px;border:1px solid rgba(255,255,255,.55);pointer-events:none}
.beam{position:absolute;left:0;right:0;
  background:radial-gradient(ellipse 40% 60% at 50% 60%,rgba(255,255,255,.85),rgba(202,222,239,.35) 45%,rgba(202,222,239,0) 75%)}
.lede{position:absolute;left:0;right:0;letter-spacing:.28em;font-weight:600;text-transform:uppercase;line-height:1.45}
.title{position:absolute;left:0;right:0;font-family:"Cinzel Decorative",serif;text-transform:uppercase;line-height:1.05}
.title__to{display:inline-block;font-family:"Great Vibes",cursive;text-transform:none;border:1px solid var(--white);border-radius:50%;vertical-align:middle;margin:2px 0}
.subline{position:absolute;left:0;right:0;text-transform:uppercase;letter-spacing:.2em;font-weight:500;line-height:1.55}
.script{position:absolute;left:0;right:0;font-family:"Great Vibes",cursive;color:var(--gold);line-height:1.05}
.movement{position:absolute;left:0;right:0;text-transform:uppercase;font-weight:700;letter-spacing:.08em}
.movement span{color:var(--gold)}
.cta{position:absolute;left:50%;transform:translateX(-50%);background:var(--navy);border:1px solid var(--white);text-transform:uppercase;font-weight:700;letter-spacing:.12em;white-space:nowrap}
.details{position:absolute;left:0;right:0;bottom:0;background:var(--band);text-transform:uppercase;font-weight:500;letter-spacing:.06em;line-height:1.7}
.details b{color:var(--gold);font-weight:700}
.web{position:absolute;left:0;right:0;text-transform:uppercase;letter-spacing:.14em;font-weight:500}
.ticket{position:absolute;left:36px;right:36px;top:258px;height:66px;border-radius:6px;
  background:linear-gradient(180deg,#f7dd7a,var(--gold) 50%,var(--gold-deep));color:var(--navy)}
.ticket__kicker{position:absolute;top:-8px;left:50%;transform:translateX(-50%);background:var(--navy);color:var(--white);font-size:6.5px;font-weight:700;letter-spacing:.14em;padding:3px 8px;white-space:nowrap;text-transform:uppercase}
.ticket__name{position:absolute;top:14px;left:0;right:0;font-family:"Cinzel Decorative",serif;font-weight:700;font-size:27px}
.ticket__note{position:absolute;top:48px;left:0;right:0;font-size:6px;font-weight:600;letter-spacing:.12em;text-transform:uppercase}
.perks{position:absolute;left:30px;right:22px;top:376px;display:grid;grid-template-columns:1fr 1fr;row-gap:8px;column-gap:8px;list-style:none;text-align:left}
.perks li{font-size:6.2px;font-weight:600;letter-spacing:.04em;text-transform:uppercase;display:flex;align-items:center;gap:4px;white-space:nowrap;line-height:1.2}
.perks svg{flex:none}
</style>
</head>
<body>
<main class="canvas">

  <section class="poster poster--hero">
    <div class="beam" style="top:250px;height:230px" role="img" aria-label="Soft beam of light rising over the water at dusk"></div>
    <div class="poster__frame"></div>
    <p class="lede" style="top:48px;font-size:19px">Let's<br>come together<br>to</p>
    <h1 class="title" style="top:150px;font-size:27px">An Evening in Linen<br><span class="title__to" style="font-size:17px;width:30px;height:30px;line-height:28px">to</span><br>Gather the Orchard</h1>
    <p class="subline" style="top:262px;font-size:8px">A fundraising gala<br>in celebration of the 150th anniversary<br>of Bramblewood Orchard</p>
    <p class="script" style="top:316px;font-size:30px">For her next 150 years to come!</p>
    <p class="movement" style="top:474px;font-size:8px;color:var(--navy)">Be part of the movement to <span style="color:var(--navy)">#SaveBramblewoodOrchard</span></p>
    <p class="web" style="top:494px;font-size:6.5px;color:var(--navy)">www.savebramblewoodorchard.org</p>
    <div class="details" style="height:62px;padding-top:10px;font-size:7.5px">
      <b>When:</b> November 16th, 2025 · Cocktails 6:30pm | VIP ticket holders 6:00pm<br>
      <b>Where:</b> Juniper Hall – 4120 Meadow Lane – Fairhaven<br>
      <b>Dress:</b> Cocktail attire · Space is limited
    </div>
  </section>

  <section class="poster poster--invite">
    <div class="beam" style="top:200px;height:200px" role="img" aria-label="Soft beam of light over the water"></div>
    <div class="poster__frame"></div>
    <p class="lede" style="top:40px;font-size:13px">Let's<br>come together<br>to</p>
    <h2 class="title" style="top:112px;font-size:19px">An Evening in Linen<br><span class="title__to" style="font-size:12px;width:22px;height:22px;line-height:20px">to</span><br>Gather the Orchard</h2>
    <p class="subline" style="top:190px;font-size:6px">A fundraising gala<br>in celebration of the 150th anniversary<br>of Bramblewood Orchard</p>
    <p class="script" style="top:240px;font-size:21px;padding:0 28px">Join us for a luminous evening of dining, delectable libations, live entertainment, artistry and more!</p>
    <div class="cta" style="top:348px;font-size:7px;padding:7px 14px">Get your tickets today!</div>
    <p class="movement" style="top:388px;font-size:10px;line-height:1.4">Be part of the movement to<br><span>#SaveBramblewoodOrchard</span></p>
    <div class="details" style="height:58px;padding-top:9px;font-size:5.6px">
      <b>When:</b> November 16th, 2025 · Cocktails 6:30pm | VIP ticket holders 6:00pm<br>
      <b>Where:</b> Juniper Hall – 4120 Meadow Lane – Fairhaven<br>
      <b>Dress:</b> Cocktail attire · Space is limited
    </div>
  </section>

  <section class="poster poster--vip">
    <div class="beam" style="top:200px;height:200px" role="img" aria-label="Soft beam of light over the water"></div>
    <div class="poster__frame"></div>
    <p class="lede" style="top:40px;font-size:13px">Let's<br>come together<br>to</p>
    <h2 class="title" style="top:112px;font-size:19px">An Evening in Linen<br><span class="title__to" style="font-size:12px;width:22px;height:22px;line-height:20px">to</span><br>Gather the Orchard</h2>
    <p class="subline" style="top:190px;font-size:6px">A fundraising gala<br>in celebration of the 150th anniversary<br>of Bramblewood Orchard</p>
    <div class="ticket">
      <span class="ticket__kicker">Gather the magic with an exclusive</span>
      <div class="ticket__name">VIP Package</div>
      <div class="ticket__note">Your golden ticket to an unforgettable night</div>
    </div>
    <div class="cta" style="top:340px;font-size:7px;padding:7px 14px">Get your tickets today!</div>
    <ul class="perks">
      <li><svg width="8" height="8" viewBox="0 0 8 8"><path d="M1 4.2l2 2 4-5" fill="none" stroke="#f2c94c" stroke-width="1.4"/></svg>VIP pre-gala experience</li>
      <li><svg width="8" height="8" viewBox="0 0 8 8"><path d="M1 4.2l2 2 4-5" fill="none" stroke="#f2c94c" stroke-width="1.4"/></svg>Exclusive dinner for 10</li>
      <li><svg width="8" height="8" viewBox="0 0 8 8"><path d="M1 4.2l2 2 4-5" fill="none" stroke="#f2c94c" stroke-width="1.4"/></svg>Unlimited premium bar</li>
      <li><svg width="8" height="8" viewBox="0 0 8 8"><path d="M1 4.2l2 2 4-5" fill="none" stroke="#f2c94c" stroke-width="1.4"/></svg>Exclusive meet &amp; greet</li>
      <li><svg width="8" height="8" viewBox="0 0 8 8"><path d="M1 4.2l2 2 4-5" fill="none" stroke="#f2c94c" stroke-width="1.4"/></svg>Dedicated wine service</li>
      <li><svg width="8" height="8" viewBox="0 0 8 8"><path d="M1 4.2l2 2 4-5" fill="none" stroke="#f2c94c" stroke-width="1.4"/></svg>Bottle of wine giveaway</li>
      <li><svg width="8" height="8" viewBox="0 0 8 8"><path d="M1 4.2l2 2 4-5" fill="none" stroke="#f2c94c" stroke-width="1.4"/></svg>Custom gift keepsake</li>
      <li><svg width="8" height="8" viewBox="0 0 8 8"><path d="M1 4.2l2 2 4-5" fill="none" stroke="#f2c94c" stroke-width="1.4"/></svg>Prime table placement</li>
    </ul>
    <div class="details" style="height:58px;padding-top:9px;font-size:5.6px">
      <b>When:</b> November 16th, 2025 · Cocktails 6:30pm | VIP ticket holders 6:00pm<br>
      <b>Where:</b> Juniper Hall – 4120 Meadow Lane – Fairhaven<br>
      <b>Dress:</b> Cocktail attire · Space is limited
    </div>
  </section>

</main>
</body>
</html>
```